Clean and modern business cards

Looking for an updated business card design for my dental office “corvanta dental” . Looking for a modern clean / sleek design . I’m thinking black background but open to seeing other options . One side needs to have an appointment card . Card needs to have logo, dentist name , phone, email , address . I’ve attached couple of cards I thought were cool as well as my logo
Target Market(s)
Dental patients
Industry/Entity Type
Dentistry
Contact Information for Business Card
Phone email address

```html
<!DOCTYPE html>
<html lang="en">
<head>
<meta charset="utf-8">
<title>Corvanta Dental – Business Card</title>
<link href="https://fonts.googleapis.com/css2?family=Poppins:wght@400;600;700&display=swap" rel="stylesheet">
<style>
  :root {
    --stage: #2a2a2a;
    --card: #1c1c1c;
    --ink: #ffffff;
    --ink-soft: #d9d9d9;
    --accent-yellow: #f2c200;
    --field: #ffffff;
    --field-ink: #555555;
    --emboss: #232323;
    --emboss-line: #2d2d2d;
    --icon-yellow: #f2c200;
    --icon-blue: #1aa3d9;
    --icon-red: #e5352b;
    --icon-green: #6cbf3d;
  }
  * { box-sizing: border-box; margin: 0; padding: 0; }
  html, body { width: 1200px; height: 1108px; overflow: hidden; }
  body {
    background: var(--stage);
    font-family: "Poppins", sans-serif;
    color: var(--ink);
    display: flex;
    align-items: center;
    justify-content: center;
    gap: 60px;
  }
  .card {
    width: 400px;
    height: 680px;
    background: var(--card);
    border-radius: 18px;
    position: relative;
    overflow: hidden;
    text-align: center;
  }

  /* Appointment side */
  .appointment { padding: 52px 36px 0; }
  .appointment__title { font-weight: 600; font-size: 19px; margin-bottom: 20px; }
  .field {
    background: var(--field);
    color: var(--field-ink);
    border-radius: 10px;
    height: 44px;
    margin-bottom: 14px;
    display: flex;
    align-items: center;
    justify-content: space-between;
    padding: 0 18px;
    font-size: 15px;
  }
  .field__label { width: 80px; text-align: left; }
  .appointment__notice {
    color: var(--accent-yellow);
    font-size: 16px;
    line-height: 1.35;
    margin-top: 12px;
  }
  .divider { width: 24px; height: 1px; background: var(--ink-soft); margin: 12px auto; }
  .contact-lines { font-size: 16px; line-height: 1.45; color: var(--ink); }
  .emboss {
    position: absolute;
    left: 30px; right: 30px; bottom: -90px;
    height: 340px;
  }

  /* Identity side */
  .identity { padding-top: 70px; }
  .brand { display: flex; flex-direction: column; align-items: center; gap: 18px; }
  .brand__dot { width: 170px; height: 170px; border-radius: 50%; border: 3px solid var(--ink); }
  .brand__name { font-weight: 600; font-size: 28px; letter-spacing: 4px; text-transform: uppercase; color: var(--ink); }
  .dentist { font-weight: 700; font-size: 22px; margin-top: 50px; text-transform: uppercase; }
  .icons { display: flex; justify-content: center; gap: 8px; margin: 14px 0 12px; }
  .icons svg { width: 20px; height: 20px; }
  .identity .contact-lines { font-size: 17px; line-height: 1.5; }
</style>
</head>
<body>

  <section class="card appointment">
    <h2 class="appointment__title">Your Next Appointment is:</h2>
    <div class="field"><span class="field__label">Date</span><span>/</span><span>/</span><span></span></div>
    <div class="field"><span class="field__label">Time</span><span>/</span><span>Am / Pm</span></div>
    <p class="appointment__notice">To Cancel or reschedule please notify us at least 48 hours prior to your scheduled appointment</p>
    <div class="divider"></div>
    <p class="contact-lines">2240 maple ridge rd, winnipeg, MB<br>(204) 555-0172<br>corvantawpg.ca<br>contact@corvantawpg.ca</p>
    <svg class="emboss" viewBox="0 0 340 340" role="img" aria-label="Embossed brand mark decoration">
      <circle cx="170" cy="170" r="160" fill="none" stroke="var(--emboss-line)" stroke-width="3"/>
      <text x="170" y="120" text-anchor="middle" font-family="Poppins, sans-serif" font-weight="600" font-size="30" letter-spacing="3" fill="var(--emboss-line)">CORVANTA DENTAL</text>
    </svg>
  </section>

  <section class="card identity">
    <div class="brand">
      <span class="brand__dot"></span>
      <span class="brand__name">Corvanta Dental</span>
    </div>
    <h1 class="dentist">Dr. Elias Verhoven</h1>
    <div class="icons">
      <svg viewBox="0 0 20 20" aria-label="Phone"><circle cx="10" cy="10" r="10" fill="var(--icon-yellow)"/><path d="M7 5.5l2 2-1 1.3a6 6 0 0 0 3.2 3.2l1.3-1 2 2-1.2 1.5C9.5 14.2 5.8 10.5 5.5 6.7z" fill="#1c1c1c"/></svg>
      <svg viewBox="0 0 20 20" aria-label="Email"><circle cx="10" cy="10" r="10" fill="var(--icon-blue)"/><rect x="5" y="6.5" width="10" height="7" fill="none" stroke="#1c1c1c" stroke-width="1.4"/><path d="M5 6.5l5 4 5-4" fill="none" stroke="#1c1c1c" stroke-width="1.4"/></svg>
      <svg viewBox="0 0 20 20" aria-label="Website"><circle cx="10" cy="10" r="10" fill="var(--icon-red)"/><circle cx="10" cy="10" r="5" fill="none" stroke="#1c1c1c" stroke-width="1.3"/><path d="M5 10h10M10 5c-2.5 3-2.5 7 0 10M10 5c2.5 3 2.5 7 0 10" fill="none" stroke="#1c1c1c" stroke-width="1.1"/></svg>
      <svg viewBox="0 0 20 20" aria-label="Location"><circle cx="10" cy="10" r="10" fill="var(--icon-green)"/><path d="M10 15.5s-4-4.2-4-7a4 4 0 0 1 8 0c0 2.8-4 7-4 7z" fill="#1c1c1c"/><circle cx="10" cy="8.5" r="1.4" fill="var(--icon-green)"/></svg>
    </div>
    <p class="contact-lines">(204) 555-0172<br>contact@corvantawpg.ca<br>corvantawpg.ca<br>2240 maple ridge rd<br>winnipeg, MB</p>
  </section>

</body>
</html>
```